An international wholesale business needs letterhead design

Logo file is attached. Please design a letterhead with the following details:

- Company Name and Logo
- Address
- VAT Registration number
- Phone No
- Website address

```html
<!DOCTYPE html>
<html lang="en">
<head>
<meta charset="utf-8">
<title>Norvale Trading Letterhead</title>
<link href="https://fonts.googleapis.com/css2?family=Arimo:wght@400&display=swap" rel="stylesheet">
<style>
  :root {
    --backdrop: #e4e4e6;
    --paper: #f4f4f5;
    --brand-red: #a41f27;
    --ink: #3d3d3f;
    --ink-soft: #4a4a4d;
    --swoosh: #c9c9cc;
    --signature-tone: #d9d9dc;
    --white: #ffffff;
  }
  * { box-sizing: border-box; margin: 0; padding: 0; }
  html, body {
    width: 1200px; height: 1141px; overflow: hidden;
    background: var(--backdrop);
    font-family: "Arimo", Arial, sans-serif;
  }
  .letterhead {
    position: absolute; left: 208px; top: 20px;
    width: 783px; height: 1100px;
    background: var(--paper);
    box-shadow: 0 4px 14px rgba(0,0,0,0.18);
    overflow: hidden;
  }
  .brand {
    position: absolute; top: 74px; left: 0; width: 100%;
    display: flex; justify-content: center; align-items: center; gap: 12px;
  }
  .brand-dot {
    width: 34px; height: 34px; border-radius: 50%;
    background: var(--brand-red);
  }
  .brand-name {
    font-size: 34px; color: var(--brand-red); letter-spacing: 1px;
  }
  .letter {
    position: absolute; left: 59px; top: 272px; width: 666px;
    color: var(--ink);
  }
  .salutation { font-size: 19px; color: var(--ink-soft); margin-bottom: 36px; }
  .letter p.body {
    font-size: 11.2px; line-height: 16.7px; text-align: justify;
    margin-bottom: 16.5px;
  }
  .closing { font-size: 11.2px; margin-top: 32px; }
  .signature {
    position: absolute; left: 53px; top: 737px;
    width: 226px; height: 63px;
    background: linear-gradient(90deg, var(--signature-tone), rgba(217,217,220,0.3));
    border-radius: 4px;
  }
  .footer {
    position: absolute; left: 0; bottom: 0; width: 783px; height: 109px;
  }
  .footer svg { position: absolute; inset: 0; }
  .footer-details {
    position: absolute; left: 0; width: 100%; top: 65px;
    text-align: center; color: var(--white);
    font-size: 13px; line-height: 18.5px;
  }
</style>
</head>
<body>
  <main class="letterhead">
    <header class="brand">
      <span class="brand-dot"></span>
      <span class="brand-name">Norvale Trading</span>
    </header>

    <section class="letter">
      <p class="salutation">Dear Mr. Carter,</p>
      <p class="body">Lorem ipsum dolor sit amet, consectetur adipiscing elit. Donec orci purus, luctus vitae dignissim eu, iaculis sed purus. Vivamus faucibus, ipsum nec aliquet viverra, leo mauris condimentum ligula, sit amet sagittis enim ligula quis arcu. Nam egestas tortor id nisi porttitor mattis. In tortor ante, ultricies in suscipit a, tempus non massa. Vivamus et auctor mi. Fusce vel massa nulla. Phasellus nec eros mauris, et scelerisque orci.</p>
      <p class="body">Donec malesuada orci vitae nulla accumsan porta a id massa. Quisque accumsan iaculis magna sit amet fringilla. Maecenas consequat, magna eget tincidunt semper, odio nibh rutrum mi, id feugiat ante nisi eu risus. Vestibulum nunc orci, rhoncus a placerat in, ultricies in mi. Cras mattis varius eros, vel fringilla nisi suscipit eget. Quisque scelerisque sagittis nulla at porttitor.</p>
      <p class="body">Sed id augue vitae urna euismod commodo aliquet a quam. Pellentesque arcu velit, cursus et malesuada ut, consequat et diam. Nullam erat sem, rhoncus id ullamcorper vitae, rhoncus et arcu. In ultricies ultricies nulla, ut rutrum nisi iaculis at. Donec eu magna a metus ornare faucibus. Fusce aliquet faucibus ultricies. Morbi semper, est id tincidunt gravida, sem arcu adipiscing lacus, ac bibendum nulla leo eu purus. Quisque nec diam sed risus consectetur a ccumsan quis quis nibh. Vestibulum id purus lorem.</p>
      <p class="body">It is a long established fact that a reader will be distracted by the readable content of a page when looking at its layout. The point of using Lorem Ipsum is that it has a more-or-less normal distribution of letters, as opposed to using 'Content here, content here', making it look like readable English. Many desktop publishing packages</p>
      <p class="body">ada ut, consequat et diam. Nullam erat sem, rhoncus id ullamcorper vitae, rhoncus et arcu. In ultricies ultricies nulla, ut rutrum nisi iaculis at. Donec eu magna a metus ornare faucibus. Fusce aliquet faucibus ultricies. Morbi semper,</p>
      <p class="closing">Sincerely,</p>
    </section>

    <div class="signature" role="img" aria-label="Handwritten signature of the sender"></div>

    <footer class="footer">
      <svg viewBox="0 0 783 109" preserveAspectRatio="none" aria-hidden="true">
        <path d="M0 2 Q390 58 783 20 L783 24 Q390 64 0 6 Z" fill="var(--swoosh)"/>
        <path d="M0 17 Q380 72 783 0 L783 109 L0 109 Z" fill="var(--brand-red)"/>
      </svg>
      <div class="footer-details">
        <p>1420 Harbor View Road, Juneau, Alaska 99801 &nbsp;| VAT Reg : 098765432</p>
        <p>P: 555-014-2287 E: info@norvaletrading.com W: norvaletrading.com</p>
      </div>
    </footer>
  </main>
</body>
</html>
```